Ironleaf Personal Training Studio Information Card

The front and back of card to give people that walk in to our gym. There are a few things to say on the card. But it also needs to be designed in an attractive way. You can make some of the information bullett points or with icons or graphics. Please look at our website at https://ironleaftraining.com/ . The card will be 4" x 9"

Target Market(s)

High End Clientele who want to train in a private gym

Industry/Entity Type

Fitness

Font styles to use
Serif
Sans Serif
Other font styles liked:
• the same font Velto uses on the zelpad

Colors
F0912C
F2A743
F7CA91
FBE8D2
FDF5EE

Requirements
Must have
• A cool look

```html
<!DOCTYPE html>
<html lang="en">
<head>
<meta charset="UTF-8">
<title>Ironleaf Personal Training Studio – Information Card</title>
<link rel="stylesheet" href="https://fonts.googleapis.com/css2?family=Barlow+Condensed:wght@400;500;600;700&family=Barlow+Semi+Condensed:wght@400&family=Bebas+Neue&display=swap">
<style>
  :root {
    --orange: #ff4a0a;
    --black: #000000;
    --white: #ffffff;
    --ink: #1c1c1c;
    --grey-text: #555555;
    --panel-light: #f1f1f1;
    --page: #e8e8e8;
  }
  * { box-sizing: border-box; margin: 0; padding: 0; }
  html, body { width: 924px; height: 1200px; overflow: hidden; }
  body { background: var(--page); font-family: "Barlow Condensed", sans-serif; }

  .card {
    position: absolute; left: 202px; top: 15px;
    width: 520px; height: 1170px;
    background: var(--white); overflow: hidden;
  }

  /* Header */
  .header { position: absolute; left: 0; top: 0; width: 520px; height: 118px; background: var(--white); }
  .brand { position: absolute; left: 40px; top: 34px; }
  .brand-name {
    display: flex; align-items: center; gap: 8px;
    font-family: "Barlow Condensed", sans-serif; font-weight: 700;
    font-size: 38px; line-height: 38px; color: var(--grey-text); letter-spacing: 1px;
  }
  .brand-mark { width: 14px; height: 14px; background: var(--orange); }
  .brand-tagline {
    margin-top: 5px; font-family: "Barlow Condensed", sans-serif; font-weight: 600;
    font-size: 8.5px; letter-spacing: 4.2px; color: var(--grey-text);
  }
  .contact { position: absolute; right: 40px; top: 28px; }
  .contact-row {
    display: flex; align-items: center; justify-content: flex-end; gap: 14px;
    height: 26px; margin-bottom: 10px;
    font-family: "Barlow Condensed", sans-serif; font-size: 19px; color: var(--grey-text);
  }
  .contact-row svg { width: 20px; height: 20px; }

  /* Hero photo */
  .hero {
    position: absolute; left: 0; top: 118px; width: 520px; height: 378px;
    background:
      radial-gradient(ellipse at 68% 55%, #b8501f 0%, rgba(120,60,30,0.6) 22%, rgba(0,0,0,0) 48%),
      linear-gradient(100deg, #2a0f08 0%, #3a2418 35%, #4a4636 70%, #6b6650 100%);
  }
  .hero-headline {
    position: absolute; left: 38px; top: 58px;
    font-family: "Bebas Neue", sans-serif; font-size: 96px; line-height: 90px;
    color: var(--white);
  }
  .hero-headline .accent { color: var(--orange); display: block; }
  .hero-headline span { display: block; }

  /* How to band */
  .start-band { position: absolute; left: 0; top: 496px; width: 520px; height: 82px; background: var(--black); }
  .start-band .tab {
    position: absolute; left: 0; top: 0; width: 198px; height: 82px; background: var(--orange);
  }
  .start-title {
    position: absolute; top: 0; height: 82px; line-height: 82px;
    font-family: "Barlow Condensed", sans-serif; font-weight: 700; font-size: 50px;
    color: var(--white); letter-spacing: 0.5px;
  }
  .start-title.how { left: 35px; }
  .start-title.get { left: 220px; }

  .intro { position: absolute; left: 0; top: 578px; width: 520px; height: 218px; background: var(--black); }
  .intro-rule { position: absolute; left: 292px; top: 2px; width: 228px; height: 4px; background: var(--orange); }
  .intro p {
    position: absolute; left: 41px; top: 35px; width: 438px;
    font-family: "Barlow Semi Condensed", sans-serif; font-size: 18.5px; line-height: 25px;
    color: var(--white); text-align: justify;
  }
  .divider { position: absolute; left: 0; top: 796px; width: 520px; height: 5px; background: var(--orange); }

  /* Benefits */
  .benefits { position: absolute; left: 0; top: 801px; width: 520px; height: 324px; }
  .benefit-list { position: absolute; left: 0; top: 0; width: 291px; height: 324px; background: var(--panel-light); list-style: none; }
  .benefit {
    position: absolute; left: 38px; display: flex; align-items: center; gap: 17px;
    font-family: "Barlow Condensed", sans-serif; font-size: 20px; line-height: 23px; color: var(--ink);
  }
  .benefit svg { width: 26px; height: 26px; flex: none; }
  .programs { position: absolute; left: 291px; top: 0; width: 229px; height: 324px; background: var(--orange); }
  .programs-notch { position: absolute; left: 270px; top: 160px; width: 42px; height: 42px; }
  .programs h2 {
    position: absolute; right: 44px; top: 26px; text-align: right;
    font-family: "Barlow Condensed", sans-serif; font-weight: 700; font-size: 36px; line-height: 45px;
    color: var(--white);
  }

  .footer {
    position: absolute; left: 0; top: 1125px; width: 520px; height: 45px; background: var(--black);
    display: flex; align-items: center; justify-content: center;
    font-family: "Barlow Condensed", sans-serif; font-size: 18px; color: var(--white); letter-spacing: 0.6px; word-spacing: 4px;
  }
</style>
</head>
<body>
<div class="card">
  <header class="header">
    <div class="brand">
      <div class="brand-name"><span class="brand-mark"></span>IRONLEAF</div>
      <div class="brand-tagline">PERSONAL TRAINING STUDIO</div>
    </div>
    <div class="contact">
      <div class="contact-row">
        <svg viewBox="0 0 24 24" fill="none" stroke="#ff4a0a" stroke-width="1.4" stroke-linejoin="round"><path d="M5 3h4l2 5-2.5 1.5a11 11 0 0 0 6 6L16 13l5 2v4a2 2 0 0 1-2 2A16 16 0 0 1 3 5a2 2 0 0 1 2-2z"/></svg>
        <span>(555) 274-0190</span>
      </div>
      <div class="contact-row">
        <svg viewBox="0 0 24 24" fill="none" stroke="#ff4a0a" stroke-width="1.4"><circle cx="12" cy="12" r="8"/></svg>
        <span>ironleafgym</span>
      </div>
    </div>
  </header>

  <section class="hero" role="img" aria-label="Photo of a woman doing a barbell lunge in a gym with weight racks behind her">
    <h1 class="hero-headline"><span>TRAIN</span><span class="accent">YOUR</span><span>SOUL</span></h1>
  </section>

  <div class="start-band">
    <div class="tab"></div>
    <div class="start-title how">HOW TO</div>
    <div class="start-title get">GET STARTED ?</div>
  </div>

  <section class="intro">
    <div class="intro-rule"></div>
    <p>We schedule prospective clients for a no cost or obligation consultation. At that consultation we will do a movement screen with you. This will allow the trainer to see what level of flexibility and strength you are currently at. You will be able to discuss your goals and other issues (injuries, etc) at that time.</p>
  </section>
  <div class="divider"></div>

  <section class="benefits">
    <ul class="benefit-list">
      <li class="benefit" style="top:34px">
        <svg viewBox="0 0 26 26" fill="none" stroke="#ff4a0a" stroke-width="1.2"><path d="M4 22c0-6 2-12 5-16h5l1 3-4 1-1 5c3-2 7-2 9 1 2 3 0 6-4 6H4z"/></svg>
        Build Strength</li>
      <li class="benefit" style="top:88px">
        <svg viewBox="0 0 26 26" fill="none" stroke="#ff4a0a" stroke-width="1.2"><circle cx="10" cy="4" r="2"/><path d="M10 7v9h8M10 11l6-3M2 22h22"/></svg>
        Increase Flexibility</li>
      <li class="benefit" style="top:142px">
        <svg viewBox="0 0 26 26" fill="none" stroke="#ff4a0a" stroke-width="1.2"><path d="M7 3h12v6a6 6 0 0 1-12 0z M7 5H3c0 3 2 5 4 5 M19 5h4c0 3-2 5-4 5 M13 15v5 M8 23h10v-3H8z"/></svg>
        Train for an Event</li>
      <li class="benefit" style="top:192px">
        <svg viewBox="0 0 26 26" fill="none" stroke="#ff4a0a" stroke-width="1.2"><rect x="3" y="4" width="16" height="18" rx="3"/><circle cx="11" cy="10" r="3"/><circle cx="20" cy="20" r="4"/><path d="M20 18v4M18.5 20.5 20 22l1.5-1.5"/></svg>
        Weight Loss</li>
      <li class="benefit" style="top:246px">
        <svg viewBox="0 0 26 26" fill="none" stroke="#ff4a0a" stroke-width="1.2"><ellipse cx="13" cy="13" rx="11" ry="5" transform="rotate(45 13 13)"/><ellipse cx="13" cy="13" rx="11" ry="5" transform="rotate(-45 13 13)"/></svg>
        <span>Improve Functional<br>&amp; Daily Movements</span></li>
    </ul>
    <div class="programs">
      <h2>CUSTOM<br>TAILORED<br>PROGRAMS<br>FOR<br>SPECIFIC<br>RESULTS</h2>
    </div>
    <svg class="programs-notch" viewBox="0 0 42 42"><polygon points="0,21 21,0 21,42" fill="#ff4a0a"/></svg>
  </section>

  <footer class="footer">For more information visit - www.ironleaftraining.com</footer>
</div>
</body>
</html>
```